Site for company producing and selling products for children's health

We need an appealing professional web site design and images for a brand new company producing and selling products focused on children’s health. The site will offer information to visitors on the company, the company’s products, and general resources related to children’s health. Additionally the site will offer e-commerce functionality to allow for ordering of the company’s products.
The content and navigation for the site will be generated by programming, such as php or asp, and therefore any images used in the navigation portions of the site should allow for HTML markup to be overlaid rather than having the text built into the image or graphic.
The design must include 2 layouts, one for the landing/home page that includes only top navigation, and an inner page layout that includes both top and left navigation.
The header area of the site should include a place for links to access the visitor’s cart and profile similar to the top sections of brightcrate.com, shopvelm.com, and gadgetharbor.com.
The landing page of the site should include some type of “changing” image area where we can include multiple image files for rotation to visitors similar to what is seen at tarvel.com or fizzberry.com. The flash/animation mechanism does not need to be provided (although it would be a plus if it was) but the design must accommodate the space for it.
The company’s colors are Orange (FF9900) and Blue (0066FF) and the logo can be viewed at http://sproutnest.com/logo.png
All CSS and markup provided must be display consistently in Internet Explorer 7+, FifeFox, Google Chrome, and Safari.
Incorporating social media links (chatterly, blipster, etc.) is desirable.
Parents who are conscious of health risks associated with children's diets and consumer food products.
E-Commerce

```html
<!DOCTYPE html>
<html lang="en">
<head>
<meta charset="utf-8">
<title>sproutnest — Home</title>
<link rel="stylesheet" href="https://fonts.googleapis.com/css2?family=Open+Sans:wght@400;600;700&family=Tinos&display=swap">
<style>
:root{
  --orange:#ff9900;
  --orange-deep:#f7960f;
  --blue:#0066ff;
  --navy:#16357a;
  --navy-light:#274f9c;
  --grey-bar:#e4e4e4;
  --grey-tab:#a9a9a9;
  --text:#222;
  --muted:#555;
  --white:#fff;
  --maroon:#a5112a;
}
*{box-sizing:border-box;margin:0;padding:0}
html,body{width:1200px;height:1018px;overflow:hidden;background:var(--white)}
body{font-family:"Open Sans",Tahoma,sans-serif;color:var(--text)}
.page{position:relative;width:1061px;height:900px;transform:scale(1.131);transform-origin:0 0}
.page>*{position:absolute}
.top-rule{left:0;top:0;width:1061px;height:1px;background:#bbb}
.cart-tab{left:843px;top:0;width:122px;height:22px;background:var(--grey-tab);border-radius:0 0 6px 6px;color:var(--white);font-size:11px;font-weight:700;display:flex;align-items:center;justify-content:center;gap:8px}
.brand{left:96px;top:58px;display:flex;align-items:center;gap:8px;font-size:24px;font-weight:700;color:var(--orange)}
.brand-mark{width:20px;height:20px;background:var(--blue)}
.account-bar{left:96px;top:110px;width:522px;height:34px;background:var(--grey-bar);display:flex;align-items:center;padding-left:18px;font-size:11px}
.account-bar a{color:var(--text);text-decoration:none}
.account-bar .sep{margin:0 17px}
.main-nav{left:618px;top:110px;width:347px;height:34px;background:var(--blue);border-radius:0 6px 0 0;display:flex}
.main-nav a{color:var(--white);font-weight:700;font-size:13px;text-decoration:none;display:flex;align-items:center;justify-content:center;border-right:1px solid rgba(255,255,255,.25)}
.main-nav a:last-child{border-right:0}
.hero-photo{left:96px;top:144px;width:522px;height:411px;background:radial-gradient(circle at 55% 45%,#f3d9c9 0,#e9c7b4 35%,#d9d6da 70%,#c9c9d2 100%)}
.hero-panel{left:618px;top:144px;width:347px;height:411px;background:linear-gradient(180deg,var(--orange) 0,var(--orange-deep) 100%);border-radius:0 0 6px 0;color:var(--white);padding:140px 14px 0 30px;font-size:25px;line-height:35px}
.hero-panel strong{font-size:30px}
.hero-notch{left:588px;top:320px}
.login-band{left:96px;top:555px;width:522px;height:35px;background:var(--blue);border-radius:0 0 0 6px;display:flex;align-items:center;padding-left:15px;gap:13px}
.field{height:22px;border-radius:11px;background:var(--white);border:1px solid #ccc;font-size:11px;color:#888;padding-left:12px;display:flex;align-items:center}
.btn-login{width:88px;height:21px;border-radius:6px;background:linear-gradient(#5fc3ff,#2aa0f0);color:var(--white);font-size:11px;display:flex;align-items:center;justify-content:center}
.search-band{left:618px;top:555px;width:347px;height:35px;background:var(--grey-bar);border-radius:0 0 6px 0;display:flex;align-items:center;padding-left:15px;gap:10px}
.btn-search{width:90px;height:23px;border-radius:6px;background:#eee;border:1px solid #ccc;color:#888;font-size:11px;display:flex;align-items:center;justify-content:center}
.promo{left:96px;top:596px;width:869px;height:146px;background:var(--navy);border-radius:5px;overflow:hidden}
.promo-arrow{position:absolute;left:0;top:0}
.promo h2{position:absolute;font-family:Tinos,"Times New Roman",serif;font-weight:400;font-size:22px;color:var(--white)}
.promo p{position:absolute;font-family:Tinos,"Times New Roman",serif;font-size:13px;color:var(--white);line-height:16px}
.promo .email{position:absolute;left:17px;top:90px;width:224px;height:23px}
.btn-join{position:absolute;left:252px;top:90px;width:90px;height:23px;border-radius:7px;background:var(--maroon);color:var(--white);font-size:11px;display:flex;align-items:center;justify-content:center}
.arrival-photo{position:absolute;left:638px;top:-4px;width:230px;height:154px;border-radius:50%;background:radial-gradient(circle,#f4f4f4 0,#e2dccf 60%,#c9b98f 100%)}
.social{left:495px;top:757px;display:flex;gap:8px;font-size:10px;color:var(--muted)}
.social span{display:flex;align-items:center;gap:3px}
.social i{width:10px;height:10px;background:var(--navy-light);display:inline-block}
.footer-rule{left:96px;top:785px;width:869px;height:1px;background:#ddd}
.footer-links{left:0;top:794px;width:1061px;text-align:center;font-size:11px;color:var(--muted)}
.footer-links a{color:var(--muted);text-decoration:none}
.footer-links .sep{margin:0 7px}
.copyright{left:0;top:817px;width:1061px;text-align:center;font-size:9px;color:var(--muted)}
</style>
</head>
<body>
<div class="page">
  <div class="top-rule"></div>
  <div class="cart-tab">
    <svg width="16" height="12" viewBox="0 0 16 12" fill="none" stroke="#fff" stroke-width="1.4"><path d="M1 1h3l2 7h7l2-5H5"/><circle cx="7" cy="10.5" r="1"/><circle cx="12" cy="10.5" r="1"/></svg>
    <span>0 items</span>
  </div>
  <div class="brand"><span class="brand-mark"></span>sproutnest</div>

  <nav class="account-bar">
    <a href="#">My Account</a><span class="sep">|</span>
    <a href="#">Order Status</a><span class="sep">|</span>
    <a href="#">Shipping Details</a><span class="sep">|</span>
    <a href="#">My Offer</a><span class="sep">|</span>
    <a href="#">Customer Service</a>
  </nav>
  <nav class="main-nav">
    <a href="#" style="width:64px">Home</a>
    <a href="#" style="width:84px">Products</a>
    <a href="#" style="width:107px">New Arrivals</a>
    <a href="#" style="width:92px">Contact Us</a>
  </nav>

  <div class="hero-photo" role="img" aria-label="Rotating banner photo: mother cuddling a smiling baby"></div>
  <div class="hero-panel"><strong>Lorem Ipsum</strong> is simply dummy text of the printing and typesetting industry.</div>
  <svg class="hero-notch" width="31" height="60" viewBox="0 0 31 60"><path d="M31 0L0 30l31 30z" fill="#ff9900"/></svg>

  <form class="login-band">
    <div class="field" style="width:188px">username</div>
    <div class="field" style="width:188px">password</div>
    <div class="btn-login">Login</div>
  </form>
  <form class="search-band">
    <div class="field" style="width:223px">Keyword or Product ID</div>
    <div class="btn-search">SEARCH</div>
  </form>

  <section class="promo">
    <svg class="promo-arrow" width="450" height="146" viewBox="0 0 450 146"><path d="M0 0h383l66 73-66 73H0z" fill="#274f9c"/></svg>
    <h2 style="left:16px;top:16px">Newsletter Sign up</h2>
    <p style="left:16px;top:53px">Be the first to hear about Tips, Trends and Exclusive Offers.</p>
    <div class="field email">E-Mail</div>
    <div class="btn-join">Join Now</div>
    <h2 style="left:467px;top:16px">New Arrival</h2>
    <p style="left:467px;top:56px">Custom made, hand crafted<br>lorem ipsum, dolor sit,<br>Praesent vestibulum,<br>Duis vel mi felis, aliquet.</p>
    <div class="arrival-photo" role="img" aria-label="Product photo: wooden rocking cradle"></div>
  </section>

  <div class="social">
    <span><i></i>linkloom</span><span><i></i>chatterly</span><span><i></i>blipster</span>
  </div>
  <div class="footer-rule"></div>
  <footer class="footer-links">
    <a href="#">Terms of Use</a><span class="sep">|</span>
    <a href="#">Privacy Policy</a><span class="sep">|</span>
    <a href="#">Social Responsibility</a><span class="sep">|</span>
    <a href="#">About Sprout Nest</a><span class="sep">|</span>
    <a href="#">Sitemap</a>
  </footer>
  <div class="copyright">Copyright ©2010 sproutnest.com</div>
</div>
</body>
</html>
```